Redesign of our homepage

We are a company that operates in the Wellness tourism sector. We are starting a project to redesign our homepage. See the screenshots. The main idea is that the banner image and the text on the banner are dynamically replaced depending on whether a user clicks on the "Thumb up" or the "Thumb down" icon.
You can see a live version of our homepage at http://demo.velqorambe.com

Requirements
Must have
• Must abide by style and look & feel of the current site.
It is important to demonstrate the functionality that enables the banner image and text being refreshed at each click of a ThumbUp or ThumbDown icons. In others words the Javascript must work.

Let me add some more context on the project.

Actually the thumb up and thumb down are possible answers to question/comment dynamically displayed at the location of the current text "Experience That Make You tell an unforgettable story".
An example of a comment/question is "I need a program that would help limit my stress levels and make me look great and feel fantastic". Or "I need an activity that will reduce my stress."
So a user would have to click on a thumb up or thumb down to approve or disapprove these questions/comments..
Based on this information, I think you could move the thumbs up to the left and right side of the text (the comment/question) respectively. And move the reset underneath in the middle.

Maybe it's a good idea to reduce the font size of that text as well.

And now to the dropdown list. We need only 2 of them, and not 3 as you have displayed.
One of them contain the list:
-- I need a weekend retreat
-- ! need a week or more retreat
The other would contain a list of countries.
The drop down values must be selected before the thumbs up and down thumbs are active.
Therefore you should move them above the question/comment text.
And finally about the thumbs and reset icons. Please put them in a round orange color and make them a bit bigger.

```html
<!DOCTYPE html>
<html lang="en">
<head>
<meta charset="utf-8">
<title>Velqorambe – Wellness Retreats</title>
<link href="https://fonts.googleapis.com/css2?family=Arimo:wght@400;700&family=Lato:wght@400;700&display=swap" rel="stylesheet">
<style>
:root{
  --orange:#f7901e;
  --orange-soft:#f6c08a;
  --text:#333333;
  --muted:#666666;
  --page:#fbf8f5;
  --white:#ffffff;
  --cyan:#1aa6c9;
  --green:#3ccb5a;
  --footer:#333333;
  --footer-text:#cfcfcf;
}
*{box-sizing:border-box;margin:0;padding:0}
html,body{width:1200px;height:3869px;overflow:hidden}
body{position:relative;background:var(--page);font-family:"Arimo",Arial,sans-serif;color:var(--text)}

/* header */
.site-header{position:absolute;left:0;top:0;width:1200px;height:92px;background:var(--white)}
.brand{position:absolute;left:113px;top:28px;display:flex;align-items:center;gap:8px;font-family:"Lato",sans-serif;font-size:30px;color:var(--orange)}
.brand-dot{width:14px;height:14px;border-radius:50%;background:var(--orange)}
.social-top{position:absolute;left:532px;top:43px;display:flex;gap:24px}
.social-top span{width:14px;height:14px;border-radius:50%;background:var(--orange)}
.btn-login,.btn-signup{position:absolute;top:33px;height:33px;border-radius:17px;display:flex;align-items:center;justify-content:center;gap:8px;font-size:15px;font-weight:700}
.btn-login{left:868px;width:105px;border:2px solid var(--orange);color:var(--orange);background:var(--white)}
.btn-signup{left:987px;width:109px;background:var(--orange);color:var(--white)}
.main-nav{position:absolute;left:0;top:92px;width:1200px;height:54px;background:var(--orange)}
.main-nav span{position:absolute;top:18px;color:var(--white);font-size:15px;font-weight:700}

/* hero */
.hero{position:absolute;left:0;top:146px;width:1200px;height:250px;background:linear-gradient(180deg,#cfe3f1 0%,#e9f1f5 35%,#8fc4cc 62%,#5b8f7a 100%)}
.hero-wave{position:absolute;left:0;top:330px;width:1200px;height:70px}
.hero-select{position:absolute;top:160px;width:290px;height:38px;border-radius:19px;background:rgba(255,255,255,.92);font-size:14px;color:var(--muted);padding:0 18px;display:flex;align-items:center;justify-content:space-between;box-shadow:0 2px 6px rgba(0,0,0,.12)}
.hero-question{position:absolute;left:330px;top:214px;width:540px;text-align:center;font-size:19px;line-height:25px;font-weight:700;color:var(--text)}
.round-btn{position:absolute;border-radius:50%;background:var(--orange);display:flex;align-items:center;justify-content:center;box-shadow:0 2px 6px rgba(0,0,0,.2)}
.thumb-down{left:250px;top:212px;width:56px;height:56px}
.thumb-up{left:894px;top:212px;width:56px;height:56px}
.reset{left:577px;top:272px;width:46px;height:46px}

/* sidebar */
.sort-by{position:absolute;left:943px;top:478px;width:105px;height:30px;border:2px solid var(--orange);border-radius:15px;color:var(--muted);font-size:16px;display:flex;align-items:center;justify-content:center;gap:6px}
.sidebar{position:absolute;left:81px;top:496px;width:313px;height:1111px;background:var(--orange);border-radius:18px}
.filter-card{position:absolute;left:36px;width:241px;background:var(--white);border-radius:10px;box-shadow:0 2px 6px rgba(0,0,0,.1)}
.filter-card h3{height:44px;line-height:44px;padding-left:24px;font-size:18px;font-weight:400;box-shadow:0 3px 4px rgba(0,0,0,.08)}
.filter-list{list-style:none;padding:18px 0 0 24px;font-size:15px}
.filter-list li{height:28px;display:flex;align-items:center;gap:7px}
.filter-list li.sub{padding-left:16px;height:22px;color:var(--orange)}
.check{width:11px;height:11px;border:1px solid #aaa;display:inline-block;flex:none}
.check.on{border-color:var(--orange);position:relative}
.check.on::after{content:"";position:absolute;left:2px;top:2px;width:5px;height:5px;background:var(--orange)}
.chev{color:var(--orange);font-size:16px;width:8px}

/* listings */
.listing{position:absolute;left:445px;width:603px;height:640px}
.listing-photo{width:603px;height:300px;border-radius:18px}
.photo-desert{background:linear-gradient(160deg,#f3e6d6 0%,#e4a460 45%,#c9782f 100%)}
.photo-valley{background:linear-gradient(180deg,#6f95c4 0%,#e4ecf2 35%,#7a8a5e 65%,#5e6e3e 100%)}
.photo-lake{background:linear-gradient(180deg,#7a9670 0%,#4d6a4b 40%,#2fa3a3 70%,#6cc6c0 100%)}
.listing-title{position:absolute;top:327px;left:0;width:603px;font-size:20px;line-height:26px;font-weight:400;text-align:justify}
.listing-title b{color:var(--orange);font-weight:400}
.price{position:absolute;top:420px;left:0;font-size:21px;color:var(--muted);font-weight:700}
.facts{position:absolute;top:467px;left:0;list-style:none;font-size:15px;color:var(--muted)}
.facts li{height:26.5px;display:flex;align-items:center;gap:10px}
.facts li::before{content:"";width:7px;height:7px;border-radius:50%;background:var(--orange)}
.btn-details{position:absolute;top:605px;left:0;width:158px;height:35px;border-radius:18px;background:var(--orange);color:var(--white);font-size:15px;display:flex;align-items:center;justify-content:center}
.feature{position:absolute;left:360px;width:200px;display:flex;align-items:center;justify-content:flex-end;gap:14px;font-size:15px;color:var(--muted);text-align:right;line-height:19px}
.feature-icon{width:48px;height:48px;flex:none;border-radius:50%;border:2px solid var(--orange);display:flex;align-items:center;justify-content:center}
.more-btn{position:absolute;left:976px;top:2603px;width:72px;height:72px;border-radius:50%;border:4px solid var(--orange);display:flex;align-items:center;justify-content:center}

/* charts */
.chart{position:absolute}
.chart-label{position:absolute;font-family:"Lato",sans-serif;font-size:15px;color:var(--text)}
.chart-center{position:absolute;font-family:"Lato",sans-serif;text-align:center;color:var(--muted);font-size:14px;line-height:17px}
.chart-center strong{display:block;color:var(--text);font-size:16px;margin-bottom:10px}
.legend{position:absolute;width:302px;height:103px;border:1.5px solid var(--orange-soft);border-radius:14px;list-style:none;padding:18px 0 0 40px;font-family:"Lato",sans-serif;font-size:14px}
.legend li{height:21px;display:flex;align-items:center;gap:10px;color:var(--orange)}
.legend li::before{content:"";width:6px;height:6px;background:currentColor}
.legend li.lg-cyan{color:var(--cyan)}
.legend li.lg-green::before{background:var(--green)}

/* footer */
.footer-wave{position:absolute;left:0;top:3370px;width:1200px;height:60px}
.site-footer{position:absolute;left:0;top:3410px;width:1200px;height:459px;background:var(--footer);font-family:"Lato",sans-serif;color:var(--footer-text)}
.site-footer h4{position:absolute;top:103px;color:var(--white);font-size:15px;font-weight:700}
.footer-about{position:absolute;left:174px;top:157px;width:212px;font-size:14px;line-height:19px;text-align:justify}
.footer-social{position:absolute;left:174px;top:238px;display:flex;gap:22px}
.footer-social span{width:14px;height:14px;border-radius:50%;background:var(--white)}
.footer-links{position:absolute;top:150px;list-style:none;font-size:15px}
.footer-links li{height:26.3px}
.newsletter-input{position:absolute;left:831px;top:160px;width:192px;height:34px;border-radius:17px;background:#ececec;color:#aaa;font-size:14px;padding-left:14px;display:flex;align-items:center}
.newsletter-btn{position:absolute;left:831px;top:208px;width:103px;height:32px;border-radius:16px;background:var(--orange);color:var(--white);font-size:15px;font-weight:700;display:flex;align-items:center;justify-content:center}
.footer-rule{position:absolute;left:0;top:372px;width:1200px;height:1px;background:#555}
.copyright{position:absolute;left:831px;top:394px;font-size:15px}
</style>
</head>
<body>

<header class="site-header">
  <div class="brand"><span class="brand-dot"></span>velqorambe</div>
  <div class="social-top"><span></span><span></span><span></span><span></span></div>
  <a class="btn-login">Login
    <svg width="18" height="16" viewBox="0 0 18 16" fill="none" stroke="currentColor" stroke-width="1.6"><circle cx="7" cy="5" r="3.5"/><path d="M1 15c0-3.5 2.7-5.5 6-5.5s6 2 6 5.5"/><path d="M13 6h4M15 4v4"/></svg>
  </a>
  <a class="btn-signup">Sign up
    <svg width="16" height="16" viewBox="0 0 16 16" fill="none" stroke="currentColor" stroke-width="1.6"><path d="M12 9v5H2V4h5"/><path d="M9 2h5v5M14 2L7 9"/></svg>
  </a>
</header>

<nav class="main-nav">
  <span style="left:293px">EUR ⌄</span>
  <span style="left:381px">WELLNESS RETREATS ⌄</span>
  <span style="left:598px">OUR CLIMATE PLEDGE</span>
  <span style="left:823px">PARTNERS</span>
</nav>

<section class="hero" role="img" aria-label="Resort terrace with parasols, sea view and tropical plants"></section>
<svg class="hero-wave" viewBox="0 0 1200 70" preserveAspectRatio="none"><path d="M0 60 C300 20 700 50 1200 0 L1200 70 L0 70Z" fill="var(--page)"/></svg>

<div class="hero-select" style="left:300px">I need a weekend retreat
  <svg width="12" height="8" viewBox="0 0 12 8" fill="none" stroke="#f7901e" stroke-width="2"><path d="M1 1l5 5 5-5"/></svg></div>
<div class="hero-select" style="left:610px">Select a country
  <svg width="12" height="8" viewBox="0 0 12 8" fill="none" stroke="#f7901e" stroke-width="2"><path d="M1 1l5 5 5-5"/></svg></div>

<p class="hero-question">I need a program that would help limit my stress levels and make me look great and feel fantastic</p>

<a class="round-btn thumb-down" aria-label="Thumb down">
  <svg width="26" height="24" viewBox="0 0 18 16" fill="#ffffff"><path d="M1 1h4v8H1zM6 1h7l3 7v2h-5l1 4-2 1-4-6z"/></svg></a>
<a class="round-btn thumb-up" aria-label="Thumb up">
  <svg width="26" height="24" viewBox="0 0 18 16" fill="#ffffff"><path d="M1 7h4v8H1zM6 15h7l3-7V6h-5l1-4-2-1-4 6z"/></svg></a>
<a class="round-btn reset" aria-label="Reset">
  <svg width="22" height="22" viewBox="0 0 22 22" fill="none" stroke="#ffffff" stroke-width="2.2" stroke-linecap="round"><path d="M4 11a7 7 0 1 0 2-5"/><path d="M5 2v4.5h4.5"/></svg></a>

<div class="sort-by">Sort By <svg width="10" height="7" viewBox="0 0 10 7" fill="none" stroke="#f7901e" stroke-width="1.5"><path d="M1 1l4 4 4-4"/></svg></div>

<aside class="sidebar">
  <div class="filter-card" style="top:40px;height:302px">
    <h3>DESTINATIONS</h3>
    <ul class="filter-list">
      <li><span class="chev">⌄</span>Europe</li>
      <li class="sub" style="margin-top:6px"><span class="check"></span>Greese</li>
      <li class="sub"><span class="check on"></span>Italy</li>
      <li class="sub"><span class="check"></span>France</li>
      <li class="sub"><span class="check"></span>United Kingdom</li>
      <li style="margin-top:8px"><span class="chev">›</span>Asia &amp; Oceania</li>
      <li><span class="chev">›</span>Africa &amp; Middle East</li>
      <li><span class="chev">›</span>Americas &amp; Caribbean</li>
    </ul>
  </div>
  <div class="filter-card" style="top:371px;height:187px">
    <h3>CATEGORIES</h3>
    <ul class="filter-list">
      <li><span class="chev">›</span>Health &amp; Wellness</li>
      <li><span class="chev">›</span>Culinary</li>
      <li><span class="chev">›</span>Safaries</li>
      <li><span class="chev">›</span>Ranch</li>
    </ul>
  </div>
  <div class="filter-card" style="top:587px;height:224px">
    <h3>DURATION</h3>
    <ul class="filter-list">
      <li><span class="check"></span>2 days</li>
      <li><span class="check"></span>From 3 to 7 Days</li>
      <li><span class="check"></span>From 1 to 2 Weeks</li>
      <li><span class="check"></span>From 2 to 3 Weeks</li>
      <li><span class="check"></span>More than 3 Weeks</li>
    </ul>
  </div>
  <div class="filter-card" style="top:839px;height:224px">
    <h3>BUDGET</h3>
    <ul class="filter-list">
      <li><span class="check"></span>Up to &nbsp;€120</li>
      <li><span class="check"></span>From &nbsp;€120 to €360</li>
      <li><span class="check"></span>From &nbsp;€360 to €1,500</li>
      <li><span class="check"></span>From €1,500 to €2,000</li>
      <li><span class="check"></span>More than €2,000</li>
    </ul>
  </div>
</aside>

<article class="listing" style="top:556px">
  <div class="listing-photo photo-desert" role="img" aria-label="Travellers riding camels across desert dunes"></div>
  <h2 class="listing-title"><b>South Africa</b> - 3 Days Big Five Tented Safari, Kruger National Park, South Africa</h2>
  <p class="price">From: &nbsp;€525.00</p>
  <ul class="facts"><li>3 days / 2 nights</li><li>Minimum number of persons: 1</li><li>Maximum group size: 8</li><li>Minimum age: 10 years</li></ul>
  <a class="btn-details">View Details</a>
  <div class="feature" style="top:413px">Flexible<br>cancellation policy<span class="feature-icon"><svg width="26" height="18" viewBox="0 0 26 18" fill="none" stroke="#f7901e" stroke-width="1.5"><rect x="1" y="1" width="24" height="16" rx="2"/><path d="M9 1v16M4 6l3 3-3 3M13 6h8M13 10h6"/></svg></span></div>
  <div class="feature" style="top:473px">Airport<br>transfer included<span class="feature-icon"><svg width="24" height="22" viewBox="0 0 24 22" fill="none" stroke="#f7901e" stroke-width="1.5"><path d="M2 12l20-9-6 16-4-6z M12 13l10-10"/></svg></span></div>
  <div class="feature" style="top:533px">Meals included<span class="feature-icon"><svg width="24" height="22" viewBox="0 0 24 22" fill="none" stroke="#f7901e" stroke-width="1.5"><path d="M3 16a9 9 0 0 1 18 0M1 16h22M12 5v2M10 20h4"/></svg></span></div>
</article>

<article class="listing" style="top:1244px">
  <div class="listing-photo photo-valley" role="img" aria-label="Green mountain valley under cloudy sky"></div>
  <h2 class="listing-title"><b>Colorado USA</b> - 2 Days Wild West Ranch Exploration And Bike Holiday</h2>
  <p class="price">From: &nbsp;€384.00</p>
  <ul class="facts"><li>3 days / 2 nights</li><li>Minimum number of persons: 1</li><li>Maximum group size: 8</li><li>Minimum age: 10 years</li></ul>
  <a class="btn-details">View Details</a>
  <div class="feature" style="top:413px">Flexible<br>cancellation policy<span class="feature-icon"><svg width="26" height="18" viewBox="0 0 26 18" fill="none" stroke="#f7901e" stroke-width="1.5"><rect x="1" y="1" width="24" height="16" rx="2"/><path d="M9 1v16M4 6l3 3-3 3M13 6h8M13 10h6"/></svg></span></div>
  <div class="feature" style="top:473px">Airport<br>transfer included<span class="feature-icon"><svg width="24" height="22" viewBox="0 0 24 22" fill="none" stroke="#f7901e" stroke-width="1.5"><path d="M2 12l20-9-6 16-4-6z M12 13l10-10"/></svg></span></div>
  <div class="feature" style="top:533px">Meals included<span class="feature-icon"><svg width="24" height="22" viewBox="0 0 24 22" fill="none" stroke="#f7901e" stroke-width="1.5"><path d="M3 16a9 9 0 0 1 18 0M1 16h22M12 5v2M10 20h4"/></svg></span></div>
</article>

<article class="listing" style="top:1941px">
  <div class="listing-photo photo-lake" role="img" aria-label="Traveller on a long boat on a turquoise lake between limestone cliffs"></div>
  <h2 class="listing-title"><b>Australia</b> - 5 Days Full Ranch Experience And Horsemanship Training In Mulla Creek, NSW, Australia</h2>
  <p class="price">From: &nbsp;€525.00</p>
  <ul class="facts"><li>5 days / 4 nights</li><li>Minimum number of persons: 1</li><li>Maximum group size: 15</li><li>Minimum age: 15 years</li></ul>
  <a class="btn-details">View Details</a>
  <div class="feature" style="top:413px">Flexible<br>cancellation policy<span class="feature-icon"><svg width="26" height="18" viewBox="0 0 26 18" fill="none" stroke="#f7901e" stroke-width="1.5"><rect x="1" y="1" width="24" height="16" rx="2"/><path d="M9 1v16M4 6l3 3-3 3M13 6h8M13 10h6"/></svg></span></div>
  <div class="feature" style="top:473px">Airport<br>transfer included<span class="feature-icon"><svg width="24" height="22" viewBox="0 0 24 22" fill="none" stroke="#f7901e" stroke-width="1.5"><path d="M2 12l20-9-6 16-4-6z M12 13l10-10"/></svg></span></div>
  <div class="feature" style="top:533px">Meals included<span class="feature-icon"><svg width="24" height="22" viewBox="0 0 24 22" fill="none" stroke="#f7901e" stroke-width="1.5"><path d="M3 16a9 9 0 0 1 18 0M1 16h22M12 5v2M10 20h4"/></svg></span></div>
</article>

<div class="more-btn"><svg width="36" height="22" viewBox="0 0 36 22" fill="none" stroke="#f7901e" stroke-width="4" stroke-linecap="round"><path d="M3 3l15 15L33 3"/></svg></div>

<svg class="chart" style="left:181px;top:2769px" width="380" height="380" viewBox="0 0 380 380">
  <g transform="rotate(-90 190 190)" fill="none" stroke-width="78">
    <circle cx="190" cy="190" r="138" stroke="var(--cyan)" stroke-dasharray="277 867"/>
    <circle cx="190" cy="190" r="138" stroke="var(--green)" stroke-dasharray="241 867" stroke-dashoffset="-277"/>
    <circle cx="190" cy="190" r="138" stroke="var(--orange)" stroke-dasharray="349 867" stroke-dashoffset="-518"/>
  </g>
</svg>
<div class="chart-center" style="left:281px;top:2933px;width:180px"><strong>Carbon Footprint</strong>Total Carbon footprint<br>from booked vacations<br>on our site</div>
<span class="chart-label" style="left:108px;top:2848px">2.11K tCO2(e)</span>
<span class="chart-label" style="left:527px;top:2860px">158 tCO2(e)</span>
<span class="chart-label" style="left:314px;top:3165px">3.01K tCO2(e)</span>
<ul class="legend" style="left:204px;top:3219px">
  <li class="lg-cyan">Yet to offset 2.99%</li>
  <li class="lg-green">Offset total by customers 57.01%</li>
  <li>Offset total by Velqorambe, 40%</li>
</ul>

<svg class="chart" style="left:704px;top:2789px" width="380" height="380" viewBox="0 0 380 380">
  <g transform="rotate(-130 190 190)" fill="none" stroke-width="78">
    <circle cx="190" cy="190" r="138" stroke="var(--cyan)" stroke-dasharray="265 867"/>
    <circle cx="190" cy="190" r="138" stroke="var(--green)" stroke-dasharray="265 867" stroke-dashoffset="-265"/>
    <circle cx="190" cy="190" r="138" stroke="var(--orange)" stroke-dasharray="337 867" stroke-dashoffset="-530"/>
  </g>
</svg>
<div class="chart-center" style="left:804px;top:2924px;width:180px"><strong>Trees</strong>Total trees to<br>offset booked vacation<br>on our site</div>
<span class="chart-label" style="left:936px;top:2769px">576 Trees</span>
<span class="chart-label" style="left:661px;top:3069px">576 Trees</span>
<span class="chart-label" style="left:1014px;top:3093px">821 Trees</span>
<ul class="legend" style="left:734px;top:3216px">
  <li class="lg-cyan">Yet to plant trees 2.99%</li>
  <li class="lg-green">Planted by customers 57.01%</li>
  <li>Planted by Velqorambe, 40%</li>
</ul>

<svg class="footer-wave" viewBox="0 0 1200 60" preserveAspectRatio="none">
  <path d="M0 30 C300 5 800 45 1200 15 L1200 60 L0 60Z" fill="var(--orange-soft)"/>
  <path d="M0 38 C300 14 800 52 1200 24 L1200 60 L0 60Z" fill="var(--footer)"/>
</svg>
<footer class="site-footer">
  <h4 style="left:177px">ABOUT US</h4>
  <p class="footer-about">VELQORAMBE B.V. is registered with the trade register of the Chamber of Commerce in Utrecht, the Netherlands</p>
  <div class="footer-social"><span></span><span></span><span></span><span></span></div>
  <h4 style="left:445px">QUICK LINKS</h4>
  <ul class="footer-links" style="left:445px"><li>Home</li><li>Services</li><li>About</li><li>Flights</li><li>Blog</li><li>Contact</li></ul>
  <h4 style="left:599px">USEFUL LINKS</h4>
  <ul class="footer-links" style="left:599px"><li>Terms &amp; Condition</li><li>Privacy Policy</li><li>Copy Rights</li></ul>
  <h4 style="left:831px">NEWSLETTER</h4>
  <div class="newsletter-input">Enter Email</div>
  <div class="newsletter-btn">Subscribe</div>
  <div class="footer-rule"></div>
  <p class="copyright">© 2020 VELQORAMBE B.V.</p>
</footer>

</body>
</html>
```